Tarn - Stationary Design/Layout

We are a well established clothing design and manufacturing company (Tarn Sourcing) based in London UK, with our own factory in Bangladesh, supplying to many fashion retailers and brands. Our factory has very high environmental and ethical standards with people at its heart. Our quality of garments are second to none.
Our new logo has been proudly developed by the Pixel Guild community last month, we are now in the second phase and need the layout designed for our letterheads, double sided business cards, compliment slip and clothing ticket. Feel as creative as you like, but make sure it looks great!!
***The Logo - the logo design and colour is set and should NOT be changed and stay on a dark grey backround. The logo artwork to use is attached.
***Details to use for the business card:
Dorian Pelham
Direct Line: 020 7946 0158
dorian@tarnsourcing-example.com
Tarn Sourching Ltd.
57 - 59 Hollin Row
Camdon . Swindon
NW9 4QT
Switchboard: 020 7946 0274
Fax: 020 7946 0274
www.tarnsourcing-example.co.uk
***Details to use for the letterhead and compliment slip:
Tarn Sourching Ltd.
57 - 59 Hollin Row
Camdon . Swindon
NW9 4QT
Fax: 020 7946 0274
www.tarnsourcing-example.co.uk
***Details for Swing Ticket:
Size: 12cm height by 5.5cm width
One side need to have just the logo without the 'Sourcing', on the other it needs to stay blank

```html
<!DOCTYPE html>
<html lang="en">
<head>
<meta charset="utf-8">
<title>Tarn Sourcing – Stationery</title>
<link rel="stylesheet" href="https://fonts.googleapis.com/css2?family=Questrial&display=swap">
<style>
  :root{
    --board:#d8d8d8;
    --paper:#ffffff;
    --charcoal:#3b3b3b;
    --ice:#a8dde0;
    --ice-faint:#d6eff0;
    --ink:#3a3a3a;
    --ink-soft:#8a8a8a;
    --shadow:3px 5px 8px rgba(0,0,0,.35);
  }
  *{margin:0;padding:0;box-sizing:border-box}
  html,body{width:1200px;height:899px;overflow:hidden;background:var(--board)}
  body{position:relative;font-family:"Questrial",sans-serif;color:var(--ink)}

  .sheet{position:absolute;background:var(--paper);box-shadow:var(--shadow)}
  .letterhead{left:33px;top:37px;width:547px;height:772px}
  .compliment-slip{left:628px;top:554px;width:543px;height:255px}

  .logo-tab{position:absolute;top:0;height:44px;background:var(--charcoal);
    border-radius:0 0 8px 8px;display:flex;align-items:center;justify-content:center}
  .letterhead .logo-tab{left:196px;width:155px}
  .compliment-slip .logo-tab{left:196px;width:151px}
  .logo-name{color:var(--ice);font-size:27px;letter-spacing:3px;line-height:1}

  .sheet-details{position:absolute;top:50px;left:0;width:100%;text-align:center;
    font-size:8px;line-height:10.5px;color:var(--ink-soft)}
  .sheet-details .company{color:var(--ink);font-size:9px}
  .sheet-details .greeting{font-size:9px;margin-top:1px}

  .card{position:absolute;width:140px;height:220px;border-radius:12px;box-shadow:var(--shadow);overflow:hidden}
  .card-front{left:646px;top:144px;background:var(--charcoal)}
  .card-front .logo-name{position:absolute;left:14px;top:18px;font-size:13px;letter-spacing:1.5px}
  .card-front .card-url{position:absolute;left:14px;bottom:14px;font-size:9px;color:var(--ice)}
  .card-back{left:798px;top:144px;width:148px;height:225px;background:var(--paper)}
  .card-back .watermark{position:absolute;left:-52px;top:86px;transform:rotate(90deg);
    font-size:60px;letter-spacing:4px;color:var(--ice-faint);line-height:1}
  .card-info{position:absolute;left:22px;font-size:8.5px;line-height:12px;color:var(--ink)}
  .card-info.person{top:16px}
  .card-info.office{top:128px}
  .card-info .name{font-size:10px;font-weight:bold}
  .card-info .role{font-size:7.5px;letter-spacing:.5px;margin-bottom:7px}
  .card-info .company{font-size:9.5px;font-weight:bold}

  .swing-ticket{position:absolute;left:999px;top:203px;width:127px;height:314px;
    background:var(--charcoal);border-radius:14px 14px 20px 20px;box-shadow:var(--shadow)}
  .swing-ticket .hole{position:absolute;left:60px;top:28px;width:16px;height:16px;border-radius:50%;
    background:var(--board);border:3px solid var(--ice)}
  .swing-ticket .ticket-name{position:absolute;left:50%;top:175px;transform:translate(-50%,-50%) rotate(-90deg);
    font-size:78px;letter-spacing:10px;color:var(--ice);line-height:1;white-space:nowrap}
  .ticket-string{position:absolute;left:0;top:0;pointer-events:none}
</style>
</head>
<body>

<section class="sheet letterhead">
  <div class="logo-tab"><span class="logo-name">TARN</span></div>
  <div class="sheet-details">
    <div class="company">Tarn Sourching Ltd.</div>
    <div>57 - 59 Hollin Row . Camdon . Swindon . NW9 4QT</div>
    <div>Switchboard 020 7946 0274 &nbsp; Fax: 020 7946 0274</div>
    <div>www.tarnsourcing-example.co.uk</div>
  </div>
</section>

<section class="card card-front">
  <span class="logo-name">Tarn Sourcing</span>
  <span class="card-url">www.tarnsourcing-example.co.uk</span>
</section>

<section class="card card-back">
  <span class="watermark" aria-hidden="true">TARN</span>
  <div class="card-info person">
    <div class="name">Dorian Pelham</div>
    <div class="role">MANAGER</div>
    <div>Direct Line: 020 7946 0158</div>
    <div>dorian@tarnsourcing-example.com</div>
  </div>
  <div class="card-info office">
    <div class="company">Tarn Sourching Ltd.</div>
    <div>57 - 59 Hollin Row</div>
    <div>Camdon . Swindon</div>
    <div>NW9 4QT</div>
    <div>Switchboard: 020 7946 0274</div>
    <div>Fax: 020 7946 0274</div>
  </div>
</section>

<section class="swing-ticket">
  <span class="hole"></span>
  <span class="ticket-name">TARN</span>
</section>

<svg class="ticket-string" width="1200" height="899" viewBox="0 0 1200 899" aria-hidden="true">
  <path d="M1062 240 C1060 170 1072 60 1086 22 C1092 12 1100 16 1099 30 C1096 90 1082 180 1073 240"
        fill="none" stroke="#2b2b2b" stroke-width="3" stroke-linecap="round"/>
</svg>

<section class="sheet compliment-slip">
  <div class="logo-tab"><span class="logo-name">TARN</span></div>
  <div class="sheet-details">
    <div class="company">Tarn Sourching Ltd.</div>
    <div>57 - 59 Hollin Row . Camdon . Swindon . NW9 4QT</div>
    <div>Switchboard 020 7946 0274 &nbsp; Fax: 020 7946 0274</div>
    <div>www.tarnsourcing-example.co.uk</div>
    <div class="greeting">With Compliments</div>
  </div>
</section>

</body>
</html>
```